R&T Architects - business card and stationary

Aloha,

We have a simple text logo, we need it incorporated into a business card and also stationary design (letterhead) if possible.

Please check out our website, rtamaui-studio.example for a little more about us. The logo we would like to use is in the upper left corner of the website. It is a simple colored logo based on the Klavica font. We are open to new logo's as well, but we want simple.

Thanks

```html
<!DOCTYPE html>
<html lang="en">
<head>
<meta charset="utf-8">
<title>R&amp;T Architects – Business Card Concepts</title>
<link rel="stylesheet" href="https://fonts.googleapis.com/css2?family=Exo+2:ital,wght@0,400;0,700;1,700&display=swap">
<style>
  :root {
    --olive: #6b5a35;
    --green: #93ad3c;
    --cream: #ede8c4;
    --white: #ffffff;
    --wood-light: #f3e9d6;
    --wood-mid: #e6d3b1;
    --ink-soft: #7d7462;
    --backdrop-center: #e9e9e9;
    --backdrop-edge: #8c8c8c;
    --deep-brown: #2d2312;
  }
  * { margin: 0; padding: 0; box-sizing: border-box; }
  html, body { width: 1001px; height: 1200px; overflow: hidden; }
  body {
    font-family: "Exo 2", sans-serif;
    background: radial-gradient(ellipse at 50% 52%, var(--backdrop-center) 0%, #c4c4c4 55%, var(--backdrop-edge) 100%);
    position: relative;
  }
  .card {
    position: absolute;
    width: 360px;
    height: 181px;
    overflow: hidden;
    background: var(--white);
    box-shadow: 0 1px 3px rgba(0,0,0,.18);
  }
  .block { position: absolute; }
  .wordmark {
    position: absolute;
    font-weight: 700;
    font-size: 18px;
    letter-spacing: .2px;
    line-height: 1;
    color: var(--olive);
    white-space: nowrap;
  }
  .url { position: absolute; font-size: 10px; line-height: 1; color: var(--olive); white-space: nowrap; }
  .name { position: absolute; font-size: 13px; line-height: 1; color: var(--green); white-space: nowrap; }
  .role { position: absolute; font-size: 8.5px; font-weight: 700; font-style: italic; line-height: 1; color: var(--green); }
  .quals { position: absolute; font-size: 7px; line-height: 1; color: #a8a8a8; white-space: nowrap; }
  .contact { position: absolute; font-size: 7.5px; line-height: 1; color: var(--ink-soft); white-space: nowrap; }
  .contact b { font-weight: 700; margin-right: 4px; }
  .services { position: absolute; font-size: 6.5px; line-height: 10px; letter-spacing: .6px; color: var(--ink-soft); }
  .on-dark { color: var(--cream); }
  .on-green-name { color: var(--olive); }
</style>
</head>
<body>

<!-- Concept 1: wood-grain front -->
<div class="card" style="left:93px; top:154px;">
  <div class="block" style="left:0; top:0; width:360px; height:61px; background:var(--olive);"></div>
  <div class="block" role="img" aria-label="Pale wood grain rings" style="left:0; top:61px; width:360px; height:40px; background:linear-gradient(90deg, var(--wood-light), var(--wood-mid) 70%, var(--wood-light));"></div>
  <div class="block" style="left:0; top:101px; width:360px; height:80px; background:var(--green);"></div>
  <div class="wordmark" style="left:30px; top:72px;">R&amp;T ARCHITECTS</div>
  <div class="url" style="left:205px; top:76px;">www.rtamaui-studio.example</div>
</div>

<!-- Concept 1: white contact back -->
<div class="card" style="left:549px; top:154px;">
  <div class="block" style="left:0; top:0; width:10px; height:49px; background:var(--olive);"></div>
  <div class="block" style="left:0; top:72px; width:10px; height:109px; background:var(--green);"></div>
  <div class="wordmark" style="left:30px; top:19px;">R&amp;T ARCHITECTS</div>
  <div class="name" style="left:30px; top:78px;">Leilani Hoapili</div>
  <div class="role" style="left:30px; top:98px;">Partner</div>
  <div class="quals" style="left:30px; top:109px;">Qualifications here</div>
  <div class="contact" style="left:167px; top:79px;">48-210 Kilohana Way</div>
  <div class="contact" style="left:167px; top:90px;">Palekai Hawaii 96800</div>
  <div class="contact" style="left:167px; top:108px;"><b>T</b>+1 808 555 0147</div>
  <div class="contact" style="left:167px; top:120px;"><b>E</b>leilani@rtamaui-studio.example</div>
  <div class="contact" style="left:167px; top:140px;">www.rtamaui-studio.example</div>
</div>

<!-- Concept 2: wood-grain contact card -->
<div class="card" style="left:93px; top:360px;">
  <div class="block" role="img" aria-label="Pale wood grain rings across the card" style="left:0; top:0; width:360px; height:181px; background:radial-gradient(ellipse at 85% 40%, var(--wood-mid), var(--wood-light) 75%);"></div>
  <div class="block" style="left:0; top:0; width:360px; height:60px; background:rgba(255,255,255,.55);"></div>
  <div class="block" style="left:0; top:0; width:10px; height:60px; background:var(--olive);"></div>
  <div class="block" style="left:0; top:60px; width:10px; height:121px; background:var(--green);"></div>
  <div class="wordmark" style="left:20px; top:22px;">R&amp;T ARCHITECTS</div>
  <div class="name" style="left:20px; top:74px;">Leilani Hoapili</div>
  <div class="role" style="left:20px; top:93px;">Partner</div>
  <div class="quals" style="left:20px; top:105px;">Qualifications here</div>
  <div class="contact" style="left:192px; top:75px;">48-210 Kilohana Way</div>
  <div class="contact" style="left:192px; top:87px;">Palekai Hawaii 96800</div>
  <div class="contact" style="left:192px; top:105px;"><b>T</b>+1 808 555 0147</div>
  <div class="contact" style="left:192px; top:117px;"><b>E</b>leilani@rtamaui-studio.example</div>
  <div class="contact" style="left:192px; top:137px;">www.rtamaui-studio.example</div>
</div>

<!-- Concept 2: colour-block back -->
<div class="card" style="left:549px; top:360px; background:var(--green);">
  <div class="block" style="left:0; top:0; width:360px; height:60px; background:var(--olive);"></div>
  <div class="block" style="left:0; top:0; width:8px; height:181px; background:var(--cream);"></div>
  <div class="wordmark on-dark" style="left:20px; top:74px;">R&amp;T ARCHITECTS</div>
  <div class="url on-dark" style="left:73px; top:95px;">www.rtamaui-studio.example</div>
</div>

<!-- Concept 3: block grid contact card -->
<div class="card" style="left:93px; top:685px;">
  <div class="block" style="left:0; top:0; width:155px; height:88px; background:var(--green);"></div>
  <div class="block" style="left:0; top:88px; width:210px; height:93px; background:var(--olive);"></div>
  <div class="block" style="left:210px; top:88px; width:150px; height:93px; background:var(--cream);"></div>
  <div class="wordmark" style="left:171px; top:70px;">R&amp;T ARCHITECTS</div>
  <div class="name on-green-name" style="left:20px; top:38px;">Leilani Hoapili</div>
  <div class="role" style="left:20px; top:55px; color:var(--cream);">Partner</div>
  <div class="quals" style="left:20px; top:67px; color:#c9d7a0;">Qualifications here</div>
  <div class="contact on-dark" style="left:20px; top:96px;">48-210 Kilohana Way</div>
  <div class="contact on-dark" style="left:20px; top:107px;">Palekai Hawaii 96800</div>
  <div class="contact on-dark" style="left:20px; top:126px;"><b>T</b>+1 808 555 0147</div>
  <div class="contact on-dark" style="left:20px; top:137px;"><b>E</b>leilani@rtamaui-studio.example</div>
  <div class="contact on-dark" style="left:20px; top:156px;">www.rtamaui-studio.example</div>
</div>

<!-- Concept 3 variant: services card -->
<div class="card" style="left:555px; top:685px;">
  <div class="block" style="left:0; top:0; width:154px; height:88px; background:var(--green);"></div>
  <div class="block" style="left:0; top:88px; width:154px; height:93px; background:var(--olive);"></div>
  <div class="wordmark" style="left:177px; top:36px;">R&amp;T ARCHITECTS</div>
  <div class="services" style="left:177px; top:64px;">ARCHITECTURE<br>INTERIOR DESIGN<br>URBAN DESIGN<br>LEED</div>
  <div class="name on-green-name" style="left:20px; top:38px;">Leilani Hoapili</div>
  <div class="role" style="left:20px; top:55px; color:var(--cream);">Partner</div>
  <div class="quals" style="left:20px; top:67px; color:#c9d7a0;">Qualifications here</div>
  <div class="contact on-dark" style="left:20px; top:96px;">48-210 Kilohana Way</div>
  <div class="contact on-dark" style="left:20px; top:107px;">Palekai Hawaii 96800</div>
  <div class="contact on-dark" style="left:20px; top:126px;"><b>T</b>+1 808 555 0147</div>
  <div class="contact on-dark" style="left:20px; top:137px;"><b>E</b>leilani@rtamaui-studio.example</div>
  <div class="contact on-dark" style="left:20px; top:156px;">www.rtamaui-studio.example</div>
</div>

<!-- Concept 3: block grid front -->
<div class="card" style="left:93px; top:890px;">
  <div class="block" style="left:0; top:0; width:96px; height:104px; background:var(--green);"></div>
  <div class="block" style="left:0; top:104px; width:150px; height:77px; background:var(--olive);"></div>
  <div class="block" style="left:150px; top:104px; width:210px; height:77px; background:var(--cream);"></div>
  <div class="wordmark" style="left:112px; top:88px;">R&amp;T ARCHITECTS</div>
  <div class="url" style="left:175px; top:112px;">www.rtamaui-studio.example</div>
</div>

<!-- Concept 4: dark back -->
<div class="card" style="left:555px; top:890px;">
  <div class="block" role="img" aria-label="Dark brown card with a faint repeating name pattern" style="left:0; top:0; width:360px; height:181px; background:linear-gradient(100deg, var(--deep-brown) 0%, #4a3c22 45%, var(--olive) 100%);"></div>
  <div class="url on-dark" style="left:0; width:360px; text-align:center; top:90px;">www.rtamaui-studio.example</div>
</div>

</body>
</html>
```